Business Card Design Project

I require a business card design that looks professional for a small building company. Calloway Builders is the name of the company and i don't want to use a house or building design for a logo. I require a logo design for the card incorporating the name Calloway Builders but designed smartly.

We are a Registered Building Practitioner so the small logo attached must also be used on the card.

We cover a large range of Building / Construction, Concrete, Steelwork. Not sure how to implement this.

Colors are flexible, maybe a dark grey background with white writting over it, but i am keen to see other options.

Thanks.

Target Market(s)

Anyone

Industry/Entity Type

Building

Requirements
Must have
• The logo attached must be incorporated - can be small
A logo for my company needs to be included - using Calloway Builders as the base with no picture of a house or buildings.

```html
<!DOCTYPE html>
<html lang="en">
<head>
<meta charset="utf-8">
<title>Calloway Builders – Business Card</title>
<link href="https://fonts.googleapis.com/css2?family=Montserrat:wght@400;500;700;800&display=swap" rel="stylesheet">
<style>
  :root {
    --backdrop: #ebeae8;
    --card: #f4f4f3;
    --ink: #4a4a4a;
    --ink-soft: #6b6b6b;
    --band: #555555;
    --on-band: #f1f1f1;
    --rule: #9a9a9a;
  }
  * { box-sizing: border-box; margin: 0; padding: 0; }
  html, body { width: 1200px; height: 1041px; overflow: hidden; }
  body {
    background: var(--backdrop);
    font-family: "Montserrat", sans-serif;
    color: var(--ink);
    position: relative;
  }
  .card {
    position: absolute;
    left: 220px;
    width: 760px;
    height: 434px;
    background: var(--card);
    box-shadow: 0 2px 10px rgba(0,0,0,0.12);
    overflow: hidden;
  }
  .card--front { top: 56px; }
  .card--back { top: 551px; }

  /* front */
  .brand-name {
    position: absolute; left: 44px; top: 62px;
    font-weight: 800; font-size: 46px; letter-spacing: 1px;
    text-transform: uppercase; color: var(--ink);
  }
  .top-band {
    position: absolute; left: 440px; right: 0; top: 132px; height: 12px;
    background: var(--band);
  }
  .badge {
    position: absolute; right: 56px; top: 26px;
  }
  .officer {
    position: absolute; left: 250px; top: 160px; width: 300px; text-align: center;
  }
  .officer__name { font-weight: 700; font-size: 22px; }
  .officer__title {
    font-size: 12px; color: var(--ink-soft); margin-top: 6px;
    padding-bottom: 10px; border-bottom: 1px solid var(--rule);
  }
  .contact {
    position: absolute; right: 44px; top: 166px; text-align: right;
    font-size: 11px; line-height: 20px; letter-spacing: 0.5px; text-transform: uppercase;
  }
  .address {
    position: absolute; left: 44px; top: 290px;
    font-size: 11px; line-height: 20px; letter-spacing: 0.5px; text-transform: uppercase;
    border-top: 1px solid var(--rule); padding-top: 8px; width: 230px;
  }
  .bottom-band {
    position: absolute; left: 0; right: 0; bottom: 0; height: 44px;
    background: var(--band); color: var(--on-band);
    display: flex; justify-content: center; align-items: center; gap: 28px;
    font-size: 11px; letter-spacing: 1px; text-transform: uppercase;
  }
  .bottom-band .divider { width: 1px; height: 14px; background: var(--on-band); }

  /* back */
  .back-mark {
    position: absolute; inset: 0;
    display: flex; flex-direction: column; align-items: center; justify-content: center; gap: 24px;
  }
  .back-mark__name {
    font-weight: 800; font-size: 40px; letter-spacing: 2px;
    text-transform: uppercase; color: var(--ink);
  }
</style>
</head>
<body>
  <section class="card card--front" aria-label="Business card front">
    <div class="brand-name">Calloway Builders</div>
    <svg class="badge" width="64" height="64" viewBox="0 0 64 64" role="img" aria-label="Registered building practitioner badge">
      <circle cx="32" cy="32" r="30" fill="none" stroke="var(--ink)" stroke-width="3"/>
    </svg>
    <div class="top-band"></div>

    <div class="officer">
      <div class="officer__name">Officer Name</div>
      <div class="officer__title">Chief Executive Officer</div>
    </div>

    <div class="contact">
      <div>Office: 555-301-4420</div>
      <div>Fax: 555-301-4421</div>
      <div>Cell: 555-918-2276</div>
    </div>

    <div class="address">
      <div>Texas</div>
      <div>2850 Millbrook Rd. Riverton,</div>
      <div>TX 78100</div>
    </div>

    <div class="bottom-band">
      <span>info@callowaybuilders.com</span>
      <span class="divider"></span>
      <span>www.callowaybuilders.com</span>
    </div>
  </section>

  <section class="card card--back" aria-label="Business card back">
    <div class="back-mark">
      <svg width="170" height="170" viewBox="0 0 170 170" aria-hidden="true">
        <circle cx="85" cy="85" r="85" fill="var(--band)"/>
      </svg>
      <div class="back-mark__name">Calloway Builders</div>
    </div>
  </section>
</body>
</html>
```